Kestrel Plumbing Solutions

This is for my new plumbing company, I have attached an example of what I’m going for but want it to look better.

Target Market(s)

Home owners, real estate, etc.

Industry/Entity Type

Plumbing

• As per my logo and other examples uploaded

Colors

Designer to choose colors to be used in the design.

Requirements
Must have
• Must include my logo provided and similar to my flyer I have attached but better

```html
<!DOCTYPE html>
<html lang="en">
<head>
<meta charset="utf-8">
<title>Kestrel Plumbing Solutions – Flyer</title>
<link href="https://fonts.googleapis.com/css2?family=Archivo:ital,wght@0,400;0,600;0,700;0,800;0,900;1,500;1,800;1,900&display=swap" rel="stylesheet">
<style>
  :root {
    --orange: #e46a32;
    --dark: #231f20;
    --tile: #1a1819;
    --ink: #111;
    --silver-1: #8d8d8d;
    --silver-2: #f4f4f4;
    --label: #d9d9d9;
    --photo-dark: #3a3d40;
    --photo-mid: #55585c;
  }
  * { margin: 0; padding: 0; box-sizing: border-box; }
  html, body { width: 846px; height: 1200px; overflow: hidden; background: #fff; }
  body { font-family: "Archivo", Arial, sans-serif; }
  .flyer { position: relative; width: 846px; height: 1200px; overflow: hidden; background: var(--dark); }

  .hero {
    position: absolute; left: 0; top: 0; width: 846px; height: 464px;
    background:
      linear-gradient(180deg, transparent 58%, rgba(228,106,50,.55) 62%, rgba(200,200,200,.45) 68%, rgba(228,106,50,.5) 74%, transparent 80%),
      radial-gradient(ellipse at 50% 40%, var(--photo-mid), var(--photo-dark));
  }
  .offer { position: absolute; left: 328px; top: 40px; width: 194px; height: 222px; }
  .offer svg { position: absolute; inset: 0; }
  .offer-text {
    position: absolute; left: 0; top: 0; width: 194px; text-align: center;
    color: #e8e8e8; transform: rotate(3deg); transform-origin: 50% 30%;
  }
  .offer-lead { font-weight: 600; font-size: 16px; line-height: 17px; margin-top: 6px; }
  .offer-value { font-weight: 900; font-size: 60px; line-height: 58px; margin-top: 6px; letter-spacing: -1px; }
  .offer-word { font-weight: 900; font-size: 26px; line-height: 28px; letter-spacing: -.5px; }

  .tagline {
    position: absolute; left: 0; top: 464px; width: 846px; height: 93px;
    background: linear-gradient(90deg, var(--silver-1), var(--silver-2) 30%, var(--silver-2) 70%, var(--silver-1));
    text-align: center; color: var(--ink);
  }
  .tagline h1 { font-weight: 900; font-style: italic; font-size: 28.5px; letter-spacing: 1.2px; margin-top: 20px; line-height: 32px; }
  .tagline p { font-style: italic; font-weight: 500; font-size: 17px; margin-top: 4px; }
  .tagline strong { font-weight: 900; }

  .services-head {
    position: absolute; left: 0; top: 557px; width: 846px; height: 50px;
    background: var(--orange); text-align: center;
    font-weight: 900; font-style: italic; font-size: 24px; line-height: 50px; color: var(--dark); letter-spacing: 1px;
  }
  .services {
    position: absolute; left: 0; top: 607px; width: 846px; height: 416px;
    display: grid; grid-template-columns: 294px 258px 294px; grid-template-rows: 146px 130px 140px;
  }
  .service {
    border-right: 1px solid var(--orange); border-bottom: 1px solid var(--orange);
    display: flex; flex-direction: column; align-items: center; padding-top: 25px;
  }
  .service:nth-child(3n) { border-right: none; }
  .service:nth-child(n+7) { border-bottom: none; }
  .service:nth-child(n+4):nth-child(-n+6) { padding-top: 11px; }
  .service:nth-child(n+7) { padding-top: 15px; }
  .icon { width: 57px; height: 57px; background: var(--tile); display: flex; align-items: center; justify-content: center; }
  .icon svg { width: 46px; height: 46px; }
  .service-name {
    margin-top: 4px; color: var(--label); font-weight: 700; font-size: 19.5px;
    line-height: 20px; text-align: center; letter-spacing: .6px;
  }

  .contact-bar { position: absolute; left: 0; top: 1023px; width: 846px; height: 10px; background: var(--orange); }
  .contact { position: absolute; left: 0; top: 1033px; width: 846px; height: 167px; background: var(--orange); }
  .contact-panel {
    position: absolute; inset: 0;
    background: linear-gradient(90deg, #e6e6e6, #a9a9a9);
    clip-path: polygon(523px 0, 846px 0, 846px 167px, 450px 167px);
  }
  .contact-list { position: absolute; left: 56px; top: 30px; color: var(--ink); }
  .row { display: flex; align-items: center; }
  .row svg { flex: none; }
  .phone { font-weight: 900; font-size: 43px; letter-spacing: 1.5px; line-height: 50px; }
  .phone svg { margin-right: 10px; }
  .email, .social { font-size: 18px; font-weight: 400; line-height: 28px; }
  .email { margin-top: 4px; }
  .email svg, .social svg { margin-right: 10px; }
  .brand {
    position: absolute; left: 560px; top: 62px; width: 240px;
    display: flex; align-items: center; gap: 10px;
    color: var(--dark); font-weight: 800; font-size: 21px; line-height: 23px; letter-spacing: .5px;
  }
  .brand-mark { width: 26px; height: 26px; background: var(--dark); flex: none; }
</style>
</head>
<body>
<main class="flyer">
  <section class="hero" role="img" aria-label="Photograph of weathered orange and grey gas pipes with valves and a wrench on a flange, against a dark granite wall">
    <div class="offer">
      <svg viewBox="0 0 194 222" aria-hidden="true">
        <path d="M42 4 L12 3 L6 150 L70 152 L94 210 L98 152" fill="none" stroke="#d8d8d8" stroke-width="7"/>
        <path d="M154 11 L186 13 L178 175 L135 173" fill="none" stroke="#d8d8d8" stroke-width="7"/>
      </svg>
      <div class="offer-text">
        <div class="offer-lead">Mention this<br>flyer to receive</div>
        <div class="offer-value">15%</div>
        <div class="offer-word">DISCOUNT</div>
      </div>
    </div>
  </section>

  <header class="tagline">
    <h1>YOUR LOCAL RELIABLE SYDNEY PLUMBER</h1>
    <p>- Specialising in all aspects of <strong>Plumbing, Drainage &amp; Gas Maintenance.</strong></p>
  </header>

  <h2 class="services-head">— OUR SERVICES —</h2>

  <section class="services">
    <div class="service">
      <div class="icon"><svg viewBox="0 0 46 46"><circle cx="28" cy="18" r="15" fill="none" stroke="#ddd" stroke-width="1.5" stroke-dasharray="3 2"/><text x="28" y="23" font-size="14" font-weight="700" fill="#eee" text-anchor="middle" font-family="Archivo, sans-serif">24</text><path d="M6 12c-2 10 6 24 18 30l5-5-6-6-4 3c-4-3-6-7-7-11l4-3-4-8z" fill="#eee"/></svg></div>
      <div class="service-name">EMERGENCY<br>PLUMBING</div>
    </div>
    <div class="service">
      <div class="icon"><svg viewBox="0 0 46 46"><circle cx="14" cy="14" r="5" fill="#ddd"/><path d="M6 40l4-16h8l6 8-3 2-5-5-2 11z" fill="#ddd"/><rect x="28" y="14" width="14" height="12" fill="#ddd"/><rect x="33" y="6" width="3" height="8" fill="#ddd"/><path d="M22 28l6 6" stroke="#ddd" stroke-width="3"/></svg></div>
      <div class="service-name">PLUMBING<br>MAINTENANCE</div>
    </div>
    <div class="service">
      <div class="icon"><svg viewBox="0 0 46 46"><rect x="6" y="4" width="8" height="14" fill="#ddd"/><path d="M8 18v6a13 13 0 0 0 26 0V14" fill="none" stroke="#ddd" stroke-width="6"/><path d="M30 10h10v6" fill="none" stroke="#ddd" stroke-width="4"/><path d="M22 36v8" stroke="#ddd" stroke-width="2"/></svg></div>
      <div class="service-name">DRAINAGE<br>MAINTENANCE</div>
    </div>
    <div class="service">
      <div class="icon"><svg viewBox="0 0 46 46"><path d="M23 4c4 9 14 16 14 27a14 14 0 0 1-28 0c0-7 5-10 6-16 2 4 3 6 5 7 0-7 1-12 3-18z" fill="#e6e6e6"/><path d="M23 26c3 4 5 6 5 10a5 5 0 0 1-10 0c0-4 3-6 5-10z" fill="#1a1819"/></svg></div>
      <div class="service-name">GAS<br>MAINTENANCE</div>
    </div>
    <div class="service">
      <div class="icon"><svg viewBox="0 0 46 46"><rect x="11" y="2" width="24" height="40" rx="3" fill="#e2e2e2"/><circle cx="23" cy="12" r="2.5" fill="none" stroke="#777" stroke-width="1.5"/><circle cx="23" cy="20" r="2.5" fill="none" stroke="#777" stroke-width="1.5"/><rect x="17" y="28" width="12" height="6" rx="1" fill="none" stroke="#777" stroke-width="1.5"/></svg></div>
      <div class="service-name">HOT WATER<br>SYSTEMS</div>
    </div>
    <div class="service">
      <div class="icon"><svg viewBox="0 0 46 46"><rect x="2" y="16" width="14" height="7" fill="#ddd"/><path d="M16 14h16a8 8 0 0 1 8 8v6h-7v-6H16z" fill="#ddd"/><rect x="22" y="8" width="4" height="6" fill="#ddd"/><rect x="17" y="5" width="14" height="3" fill="#ddd"/><path d="M36 32c1 3 2 4 0 6-2-2-1-3 0-6z" fill="#ddd"/></svg></div>
      <div class="service-name">LEAKING<br>FIXTURES</div>
    </div>
    <div class="service">
      <div class="icon"><svg viewBox="0 0 46 46"><circle cx="4" cy="24" r="1.5" fill="#ddd"/><rect x="9" y="19" width="6" height="10" fill="#ddd"/><circle cx="27" cy="24" r="10" fill="none" stroke="#ddd" stroke-width="3"/><circle cx="27" cy="24" r="4" fill="none" stroke="#ddd" stroke-width="2"/><path d="M33 14l7-4v10" fill="none" stroke="#ddd" stroke-width="3"/></svg></div>
      <div class="service-name">BLOCKED SEWER &amp;<br>STORMWATER</div>
    </div>
    <div class="service">
      <div class="icon"><svg viewBox="0 0 46 46" fill="none" stroke="#ddd" stroke-width="3" stroke-linecap="round"><path d="M4 14a28 28 0 0 1 38 0"/><path d="M10 21a19 19 0 0 1 26 0"/><path d="M16 28a10 10 0 0 1 14 0"/><circle cx="23" cy="38" r="4"/></svg></div>
      <div class="service-name">CAMERA &amp;<br>LOCATING</div>
    </div>
    <div class="service">
      <div class="icon"><svg viewBox="0 0 46 46" fill="none" stroke="#ddd" stroke-width="2"><path d="M18 6c5 9 11 14 11 22a11 11 0 0 1-22 0c0-8 6-13 11-22z"/><rect x="28" y="10" width="7" height="24" rx="3.5" fill="#1a1819"/><circle cx="31.5" cy="37" r="5" fill="#ddd"/></svg></div>
      <div class="service-name">TMV<br>MAINTENANCE</div>
    </div>
  </section>

  <div class="contact-bar"></div>
  <footer class="contact">
    <div class="contact-panel"></div>
    <div class="contact-list">
      <div class="row phone">
        <svg width="30" height="30" viewBox="0 0 30 30"><path d="M5 4c-3 9 5 20 16 23l4-5-6-4-3 2c-3-2-5-5-6-8l3-2-3-7z" fill="none" stroke="#111" stroke-width="2.6"/><path d="M18 4a9 9 0 0 1 8 8M18 9a4 4 0 0 1 3 3" fill="none" stroke="#111" stroke-width="2"/></svg>
        0400 555 218
      </div>
      <div class="row email">
        <svg width="29" height="20" viewBox="0 0 29 20"><rect x="1" y="1" width="27" height="18" fill="none" stroke="#111" stroke-width="2"/><path d="M1 1l13.5 11L28 1M1 19l10-9M28 19l-10-9" fill="none" stroke="#111" stroke-width="2"/></svg>
        kestrelplumbingsolutions@mailbox.net
      </div>
      <div class="row social">
        <svg width="29" height="29" viewBox="0 0 29 29"><circle cx="14.5" cy="14.5" r="14" fill="#111"/></svg>
        @KestrelPlumbingSolutions
      </div>
    </div>
    <div class="brand">
      <span class="brand-mark"></span>
      <span>KESTREL<br>PLUMBING SOLUTIONS</span>
    </div>
  </footer>
</main>
</body>
</html>
```